We need a web design for a retail food business based in Greater Western Sydney Australia called Golden Lantern Chinese Restaurant. Basically just need a simple yet easily to navigate website to browse through a menu, gallery , brief description about us, opening hours.
Menu and Gallery will be constantly updated.
Will provide own images for gallery
Updates
Menu has been uploaded and some idea on the colours I would like on the site
Some additional pictures added to see what designs you guys can come up with . Thanks again
To All Designers,
Any extra fee on top of the designs that feels need to be charged, please let me know in advance
Reason: Extending Deadline as I have yet to find a design that I would like...Thanks guys
Target Market(s)
All groups
Industry/Entity Type
Business
Requirements
Must have
- Open minded to any designs
Nice to have
- Would like slideshow behind main logo.
Preferred light coloured site yet not too playful
Should not have
- Preferably no dark colours backgrounds

```html
<!DOCTYPE html>
<html lang="en">
<head>
<meta charset="utf-8">
<title>Golden Lantern Chinese Restaurant</title>
<link href="https://fonts.googleapis.com/css2?family=Arimo:wght@400;700&display=swap" rel="stylesheet">
<style>
:root{
  --page:#fff4dc;
  --page-edge:#fbe6bd;
  --ink:#6e1a0c;
  --red:#c0181a;
  --red-soft:#d8321f;
  --orange:#f08a00;
  --orange-deep:#d46400;
  --gold:#ffc400;
  --yellow:#ffd21c;
  --white:#ffffff;
  --text-light:#fff2c8;
  --footer:#f3d9a8;
}
*{box-sizing:border-box;margin:0;padding:0}
html,body{width:738px;height:1200px;overflow:hidden}
body{
  position:relative;
  font-family:"Arimo",Arial,sans-serif;
  color:var(--ink);
  background:linear-gradient(180deg,var(--page) 0%,var(--page-edge) 100%);
}
.abs{position:absolute}

/* hero band */
.hero-band{left:0;top:0;width:738px;height:400px;
  background:
    radial-gradient(ellipse 360px 280px at 330px 170px,#ffd34a 0%,#ffb020 40%,rgba(255,150,30,0) 80%),
    linear-gradient(180deg,#f27a22 0%,#e8601c 100%)}

/* header */
.brand{left:6px;top:27px;width:213px;height:108px;border-radius:10px;overflow:hidden;
  background:linear-gradient(180deg,var(--yellow),var(--orange));box-shadow:0 2px 6px rgba(0,0,0,.3)}
.brand-name{position:absolute;left:14px;top:12px;font-weight:700;font-size:27px;line-height:31px;color:var(--white);text-transform:uppercase}
.brand-tagline{position:absolute;left:0;bottom:0;width:100%;height:28px;background:var(--red);
  font-size:11px;color:var(--yellow);text-align:center;line-height:28px}
.locale{right:22px;top:26px;display:flex;align-items:center;gap:5px;font-size:9px;color:var(--white)}
.flag{width:12px;height:8px;border-radius:1px}
.currency-select{width:72px;height:15px;background:var(--white);color:#888;font-size:9px;padding-left:4px;line-height:15px;margin-left:4px}
.welcome{right:22px;top:52px;font-size:9px;color:var(--white)}
.account{right:22px;top:68px;display:flex;align-items:center;gap:8px;font-size:9px;color:var(--yellow)}
.account b{font-size:20px;color:var(--yellow)}
.account .items{color:var(--white)}
.nav{left:486px;top:98px;display:flex;gap:3px}
.nav a{width:55px;height:37px;border-radius:10px 10px 4px 4px;background:linear-gradient(180deg,var(--yellow),var(--orange));
  color:var(--white);font-weight:700;font-size:9.5px;line-height:37px;text-align:center;text-decoration:none;white-space:nowrap}
.nav a.active{background:linear-gradient(180deg,#fff,#ffe9c0);color:var(--orange)}

/* hero */
.hero-photo{left:190px;top:0;width:277px;height:396px;
  background:radial-gradient(ellipse at 50% 45%,#ffd070 0%,#f0a030 50%,rgba(240,120,30,0) 85%)}
.hero-title{left:22px;top:174px;font-size:38px;font-weight:700;color:var(--white)}
.steps{left:26px;top:226px;list-style:none;color:var(--white)}
.steps li{display:flex;align-items:center;gap:8px;font-size:17px;line-height:19px;height:46px}
.step-num{width:30px;height:30px;border-radius:50%;background:var(--gold);color:var(--red);font-weight:700;font-size:18px;text-align:center;line-height:30px;flex:none}
.delivery{left:465px;top:246px;width:230px;height:121px;border-radius:12px;background:var(--red);box-shadow:0 2px 8px rgba(0,0,0,.3);padding:14px 0 0 18px;color:var(--white)}
.delivery h2{font-size:27px;font-weight:400}
.phone{display:flex;align-items:center;gap:8px;margin-top:6px;font-size:20px;font-weight:700;color:var(--gold)}
.phone-icon{width:26px;height:30px;border-radius:4px;background:var(--orange);display:flex;align-items:center;justify-content:center}
.delivery p{font-size:10px;margin-top:9px}

/* slider */
.slider{left:0;top:396px;width:717px;height:213px;background:linear-gradient(180deg,var(--yellow),var(--orange));border-radius:0 12px 12px 0}
.slider-arrow{top:476px;width:0;height:0;border-top:22px solid transparent;border-bottom:22px solid transparent}
.slider-arrow.prev{left:0;border-right:14px solid var(--red)}
.slider-arrow.next{left:705px;border-left:14px solid var(--red)}
.dish{top:418px;width:157px;height:185px;background:var(--white);padding:6px;color:var(--white)}
.dish-photo{width:100%;height:111px;border-radius:8px 8px 0 0}
.dish-info{position:absolute;left:6px;right:6px;top:117px;bottom:6px;background:var(--red);padding:6px 8px}
.dish-info h3{font-size:9px;color:var(--gold);font-weight:700}
.dish-info p{font-size:8.5px;line-height:10px;width:92px;margin-top:2px}
.dish-info .price{position:absolute;left:8px;bottom:4px;font-size:16px;font-weight:700}
.cart-badge{position:absolute;right:8px;top:96px;width:44px;height:44px;border-radius:50%;background:var(--white);display:flex;align-items:center;justify-content:center}

/* sidebar */
.search{left:27px;top:630px;width:158px;height:39px;border-radius:8px;background:var(--gold);padding:6px}
.search-field{height:27px;background:var(--white);border-radius:3px;margin-right:28px}
.search-btn{position:absolute;right:6px;top:6px;width:27px;height:27px;background:var(--red);display:flex;align-items:center;justify-content:center;border-radius:3px}
.panel-head{height:43px;border-radius:8px;background:linear-gradient(180deg,var(--red-soft),var(--red));color:var(--white);font-weight:700;font-size:12px;line-height:43px;padding-left:14px;box-shadow:0 2px 4px rgba(0,0,0,.2)}
.categories{left:27px;top:677px;width:158px}
.category-list{list-style:none;margin-top:12px;padding-left:14px}
.category-list li{display:flex;align-items:center;gap:7px;font-size:10px;height:21px;color:var(--ink)}
.category-list li::before{content:"";width:11px;height:11px;border-radius:50%;background:var(--orange)}

/* featured */
.section-title{left:205px;top:643px;font-size:12px;font-weight:700;color:var(--ink)}
.product{width:163px;height:127px;background:var(--white);border-radius:10px;padding:8px;box-shadow:0 1px 4px rgba(110,26,12,.25)}
.product-photo{width:100%;height:100%;border-radius:4px}
.product-name{font-size:9px;font-weight:700;color:var(--orange-deep)}
.product-desc{font-size:8.5px;line-height:10px;width:150px;color:var(--ink)}
.product-price{font-size:16px;font-weight:700;color:var(--orange-deep)}
.btn{display:block;background:linear-gradient(180deg,var(--yellow),var(--orange));color:var(--white);font-weight:700;font-size:9.5px;text-align:center;border-radius:2px}
.add-btn{width:115px;height:26px;line-height:26px;margin-top:2px}

/* cart */
.cart{left:533px;top:630px;width:162px}
.cart-empty{font-size:8px;color:var(--orange-deep);margin:16px 0 0 14px;font-weight:700}
.cart-row{display:flex;height:26px;margin:4px 0 0 14px;width:133px}
.cart-row span{flex:none;width:68px;background:var(--red);color:var(--white);font-size:8.5px;line-height:26px;padding-left:8px;font-weight:700}
.cart-row em{flex:1;background:var(--white);color:var(--red);font-style:normal;font-size:8.5px;line-height:26px;padding-left:8px;font-weight:700;border:1px solid #f0d0a0}
.cart-btn{margin:8px 0 0 13px;height:25px;line-height:25px;padding:0 10px;display:inline-block}

.footer{left:0;top:1150px;width:738px;height:50px;background:var(--footer)}
</style>
</head>
<body>

<div class="abs hero-band"></div>

<header>
  <div class="abs brand">
    <div class="brand-name">Golden<br>Lantern</div>
    <div class="brand-tagline">The biggest choice on the web</div>
  </div>

  <div class="abs locale">
    <span class="flag" style="background:#3a5aa8"></span>
    <span class="flag" style="background:#e8e8ff"></span>
    <span class="flag" style="background:#e0a000"></span>
    <span style="margin-left:10px">Currency:</span>
    <span class="currency-select">Dollar</span>
  </div>
  <div class="abs welcome">Welcome, ( log in )</div>
  <div class="abs account">Your Account <b>0</b> <span class="items">items</span></div>

  <nav class="abs nav">
    <a class="active" href="#">MENU</a>
    <a href="#">GALLERY</a>
    <a href="#">ABOUT US</a>
    <a href="#">HOURS</a>
  </nav>
</header>

<section class="hero">
  <div class="abs hero-photo" role="img" aria-label="Photo of a woman in a black qipao holding a bowl of noodle salad and chopsticks"></div>
  <h1 class="abs hero-title">It’s Easy!</h1>
  <ol class="abs steps">
    <li><span class="step-num">1</span>Choose<br>The Stuffing</li>
    <li><span class="step-num">2</span>Make an Order</li>
    <li><span class="step-num">3</span>Enjoy The<br>Excellent Taste</li>
  </ol>
  <div class="abs delivery">
    <h2>Order Delivery</h2>
    <div class="phone">
      <span class="phone-icon"><svg width="16" height="18" viewBox="0 0 16 18"><path d="M4 1 L7 5 L5 7 Q7 11 10 13 L12 11 L15 14 L13 17 Q6 16 2 8 Q1 4 4 1Z" fill="#fff"/></svg></span>
      +1234-5550147
    </div>
    <p>7 days a week from 8:00 a.m. to 11:00 p.m.</p>
  </div>
</section>

<section class="specials">
  <div class="abs slider"></div>
  <span class="abs slider-arrow prev"></span>
  <span class="abs slider-arrow next"></span>

  <article class="abs dish" style="left:31px">
    <div class="dish-photo" role="img" aria-label="Photo of meat sauce pasta dinner" style="background:linear-gradient(135deg,#f3e0c0,#c84020)"></div>
    <div class="dish-info"><h3>Meat Sauce Dinner</h3><p>Pellentesque felis ipsum...</p><span class="price">$13.00</span></div>
    <span class="cart-badge"><svg width="26" height="22" viewBox="0 0 26 22"><path d="M1 2h4l3 12h13l3-9H7" fill="none" stroke="#f0a000" stroke-width="2.5"/><circle cx="10" cy="19" r="2" fill="#f0a000"/><circle cx="19" cy="19" r="2" fill="#f0a000"/></svg></span>
  </article>
  <article class="abs dish" style="left:199px">
    <div class="dish-photo" role="img" aria-label="Photo of sliced veal roll" style="background:linear-gradient(135deg,#d89070,#8a3a20)"></div>
    <div class="dish-info"><h3>Veal Roll</h3><p>Donec ac turpis eget arcu...</p><span class="price">$10.00</span></div>
    <span class="cart-badge"><svg width="26" height="22" viewBox="0 0 26 22"><path d="M1 2h4l3 12h13l3-9H7" fill="none" stroke="#f0a000" stroke-width="2.5"/><circle cx="10" cy="19" r="2" fill="#f0a000"/><circle cx="19" cy="19" r="2" fill="#f0a000"/></svg></span>
  </article>
  <article class="abs dish" style="left:369px">
    <div class="dish-photo" role="img" aria-label="Photo of fried chicken pieces" style="background:linear-gradient(135deg,#e0a050,#9a5010)"></div>
    <div class="dish-info"><h3>Fried Chicken</h3><p>Aenean vulputate nisi dapibus...</p><span class="price">$10.00</span></div>
    <span class="cart-badge"><svg width="26" height="22" viewBox="0 0 26 22"><path d="M1 2h4l3 12h13l3-9H7" fill="none" stroke="#f0a000" stroke-width="2.5"/><circle cx="10" cy="19" r="2" fill="#f0a000"/><circle cx="19" cy="19" r="2" fill="#f0a000"/></svg></span>
  </article>
  <article class="abs dish" style="left:537px">
    <div class="dish-photo" role="img" aria-label="Photo of baked lasagna" style="background:linear-gradient(135deg,#e8c890,#b04818)"></div>
    <div class="dish-info"><h3>Baked Lasagna</h3><p>Lorem ipsum dolor sit amet...</p><span class="price">$10.00</span></div>
    <span class="cart-badge"><svg width="26" height="22" viewBox="0 0 26 22"><path d="M1 2h4l3 12h13l3-9H7" fill="none" stroke="#f0a000" stroke-width="2.5"/><circle cx="10" cy="19" r="2" fill="#f0a000"/><circle cx="19" cy="19" r="2" fill="#f0a000"/></svg></span>
  </article>
</section>

<aside>
  <div class="abs search">
    <div class="search-field"></div>
    <span class="search-btn"><svg width="14" height="14" viewBox="0 0 14 14"><circle cx="6" cy="6" r="4" fill="none" stroke="#fff" stroke-width="2"/><path d="M9 9l4 4" stroke="#fff" stroke-width="2"/></svg></span>
  </div>
  <div class="abs categories">
    <div class="panel-head">CATEGORIES</div>
    <ul class="category-list">
      <li>Appetizers</li><li>Beverages</li><li>Desserts</li><li>Entrees</li><li>Fruits/Vegetables</li>
      <li>Ice Cream</li><li>Meat</li><li>Seafood</li><li>Side Dishes</li><li>Snacks</li>
    </ul>
  </div>
</aside>

<main>
  <h2 class="abs section-title">FEATURED PRODUCTS</h2>

  <div class="abs product" style="left:194px;top:679px"><div class="product-photo" role="img" aria-label="Photo of drunken noodles" style="background:linear-gradient(135deg,#f0d8a0,#c06030)"></div></div>
  <div class="abs" style="left:202px;top:811px">
    <div class="product-name">Drunken Noodles</div>
    <p class="product-desc">Lorem ipsum dolor sit amet, consectetur adipiscing elit. Ut...</p>
    <div class="product-price">$6.16</div>
    <span class="btn add-btn">ADD TO CART</span>
  </div>

  <div class="abs product" style="left:364px;top:679px"><div class="product-photo" role="img" aria-label="Photo of chicken lo mein" style="background:linear-gradient(135deg,#f0e0b0,#a86030)"></div></div>
  <div class="abs" style="left:371px;top:811px">
    <div class="product-name">Chicken Lo Mein</div>
    <p class="product-desc">Mauris pharetra dictum nibh in tincidunt. Fusce at velit at...</p>
    <div class="product-price">$5.00</div>
    <span class="btn add-btn">ADD TO CART</span>
  </div>

  <div class="abs product" style="left:194px;top:916px"><div class="product-photo" role="img" aria-label="Photo of sweet and sour chicken with rice" style="background:linear-gradient(135deg,#f6ecd0,#e09020)"></div></div>
  <div class="abs" style="left:202px;top:1049px">
    <div class="product-name">Sweet and Sour Chicken Dinner</div>
    <p class="product-desc">Donec ac turpis eget arcu rutrum iaculis. Pellentesque...</p>
    <div class="product-price">$6.40</div>
    <span class="btn add-btn">ADD TO CART</span>
  </div>

  <div class="abs product" style="left:364px;top:916px"><div class="product-photo" role="img" aria-label="Photo of glazed chicken wings with dip" style="background:linear-gradient(135deg,#e8c8a0,#902810)"></div></div>
  <div class="abs" style="left:371px;top:1049px">
    <div class="product-name">Dolore magnaorem</div>
    <p class="product-desc">Proin vehicula, odio a hendrerit faucibus, sapien nulla...</p>
    <div class="product-price">$9.00</div>
    <span class="btn add-btn">ADD TO CART</span>
  </div>
</main>

<aside class="abs cart">
  <div class="panel-head">CART</div>
  <div class="cart-empty">No products</div>
  <div class="cart-row"><span>Shipping</span><em>$0.00</em></div>
  <div class="cart-row"><span>Total</span><em>$0.00</em></div>
  <span class="btn cart-btn">CART</span><br>
  <span class="btn cart-btn" style="margin-top:6px">CHECK OUT</span>
</aside>

<footer class="abs footer"></footer>
</body>
</html>
```